Training Company Needs a Web Design

We are a Training company that needs a website design completed for us. "The Harbor Loft" The website will be a 'community space' specialising in 'Change and Transformation'. It will be a 'space' where individuals can come to find out 'latest news', upcoming events and courses, chat with others and find 'tools and templates'. They will need to login as a 'Member'.

The final design needs to be professional but have a 'fun and interactive' feel and appeal to our target audience who are predominantly corporate individuals.

Target Market(s)

Corporate Individuals - they may have a Change or Project background

Industry/Entity Type

Business Consultant

Number of Pages Required

3 page

Font styles to use
Sans Serif

Requirements
Must have
• Design for 'Home Page'
• A professional and corporate 'feel' but be fun and interactive.
Nice to have
• A 'sense' of how some of the other pages may be designed or laid out.

```html
<!DOCTYPE html>
<html lang="en">
<head>
<meta charset="utf-8">
<title>The Harbor Loft — Home</title>
<link href="https://fonts.googleapis.com/css2?family=Open+Sans:wght@400;600;700&display=swap" rel="stylesheet">
<style>
:root{
  --teal:#2bb3b1;
  --blue:#1fa3d6;
  --orange:#f7931e;
  --navy:#0d3b6c;
  --navy-deep:#092e57;
  --ink:#333a40;
  --muted:#6b7177;
  --line:#e3e6e8;
  --white:#ffffff;
}
*{box-sizing:border-box;margin:0;padding:0}
html,body{width:1200px;height:2970px;overflow:hidden}
body{font-family:'Open Sans',Arial,sans-serif;color:var(--ink);background:var(--white);position:relative}
.abs{position:absolute}

/* header */
.site-header{position:absolute;top:0;left:0;width:1200px;height:76px;background:var(--white)}
.brand{position:absolute;left:100px;top:18px;display:flex;align-items:center;gap:10px}
.brand-mark{width:34px;height:34px;border-radius:50%;background:var(--blue)}
.brand-name{font-size:15px;font-weight:600;color:var(--blue);line-height:1.05;width:90px}
.main-nav{position:absolute;top:30px;left:316px;display:flex;gap:0}
.main-nav a{font-size:13px;color:var(--ink);text-decoration:none;margin-right:50px}
.btn-head{position:absolute;top:20px;height:38px;background:var(--blue);color:#fff;font-size:11px;font-weight:700;display:flex;align-items:center;justify-content:center;text-transform:uppercase;border-radius:2px}

/* hero */
.hero{position:absolute;top:76px;left:0;width:1200px;height:510px;background:linear-gradient(100deg,#c9c5c1 0%,#e9eaea 30%,#f3f4f4 50%,#d8dde2 70%,#6b7a90 100%)}
.upload-panel{position:absolute;left:266px;top:290px;width:670px;height:140px;background:rgba(255,255,255,.92);border-radius:4px}
.upload-title{position:absolute;left:24px;top:28px;font-size:16px;font-weight:700;color:var(--blue);text-transform:uppercase}
.upload-input{position:absolute;left:24px;top:64px;width:496px;height:46px;border:1px solid #ccd1d5;background:#fff;border-radius:2px;display:flex;align-items:center;padding-left:14px;gap:8px;color:#8a8f94;font-size:13px}
.upload-submit{position:absolute;left:526px;top:64px;width:120px;height:46px;background:var(--orange);color:#fff;font-size:12px;font-weight:700;display:flex;align-items:center;justify-content:center;text-transform:uppercase;border-radius:2px}
.hero-dots{position:absolute;top:488px;left:590px;display:flex;gap:8px}
.hero-dots span{width:7px;height:7px;border-radius:50%;background:rgba(255,255,255,.6)}
.hero-dots span.on{background:#fff}

/* coaching band */
.coaching{position:absolute;top:586px;left:0;width:1200px;height:100px;background:var(--teal);color:#fff}
.coaching p{position:absolute;left:100px;top:22px;width:820px;font-size:13px;line-height:26px}
.coaching strong{font-size:21px;font-weight:700;margin-right:6px;text-transform:uppercase}
.btn-outline{position:absolute;left:958px;top:26px;width:142px;height:46px;border:1px solid #fff;display:flex;align-items:center;justify-content:center;font-size:13px;font-weight:600;text-transform:uppercase}

/* section heads */
.section-title{position:absolute;left:0;width:1200px;text-align:center;font-size:23px;font-weight:700;text-transform:uppercase;color:var(--ink)}
.section-sub{position:absolute;left:0;width:1200px;text-align:center;font-size:12px;color:var(--muted)}

/* features */
.feature{position:absolute;width:300px}
.feature svg{position:absolute;left:0;top:0;width:34px;height:34px}
.feature h3{margin-left:50px;font-size:13px;font-weight:600;color:var(--ink)}
.feature p{margin-left:50px;margin-top:12px;font-size:11px;line-height:22px;color:var(--muted)}

/* cards */
.thumb{position:absolute;width:232px;height:164px}
.thumb-caption{position:absolute;width:232px;font-size:12px;font-weight:600;line-height:22px;color:var(--ink)}
.event-date{position:absolute;width:232px;font-size:12px;color:var(--muted)}

/* news */
.news{position:absolute;top:1794px;left:0;width:1200px;height:406px;background:linear-gradient(100deg,#1f4a78 0%,#2d5c8c 45%,#355f88 70%,#234c7a 100%)}
.news .section-title{color:#fff;top:62px}
.news .section-sub{color:#e6ecf2;top:110px;font-size:13px}
.news-card{position:absolute;top:168px;width:314px;height:166px;background:#fff;padding:20px 24px}
.news-card h3{font-size:12px;font-weight:600;color:var(--ink)}
.news-date{display:inline-block;margin-top:12px;background:var(--teal);color:#fff;font-size:10px;padding:4px 14px}
.news-card p{margin-top:10px;font-size:11px;line-height:22px;color:var(--muted)}

/* footer */
.site-footer{position:absolute;top:2656px;left:0;width:1200px;height:266px;background:var(--navy);color:#fff}
.foot-head{position:absolute;top:40px;font-size:12px;font-weight:700;text-transform:uppercase}
.foot-list{position:absolute;top:68px;list-style:none;font-size:11px;line-height:22px;color:#9fb6cf}
.quote{position:absolute;left:124px;top:82px;width:260px;font-size:11px;font-style:italic;line-height:19px;color:#9fb6cf}
.quote-mark{position:absolute;font-size:26px;color:#6f8fb1;font-family:Georgia,serif}
.author{position:absolute;left:122px;top:206px;font-size:11px;color:#9fb6cf}
.author b{color:#6f8fb1;text-transform:uppercase;margin-right:4px}
.social{position:absolute;left:930px;display:flex;align-items:center;gap:10px;font-size:11px;color:#9fb6cf}
.social span.dot{width:30px;height:30px;border-radius:50%;background:#3f6690}
.site-bottom{position:absolute;top:2922px;left:0;width:1200px;height:48px;background:var(--navy-deep);color:#7f9bb9;font-size:11px;display:flex;align-items:center;justify-content:center}
</style>
</head>
<body>

<header class="site-header">
  <div class="brand"><span class="brand-mark"></span><span class="brand-name">The Harbor Loft</span></div>
  <nav class="main-nav">
    <a href="#">About us</a><a href="#">Services</a><a href="#">News</a><a href="#">Events</a><a href="#">Courses</a>
  </nav>
  <a class="btn-head" style="left:784px;width:182px">New members register</a>
  <a class="btn-head" style="left:974px;width:128px">Members login</a>
</header>

<section class="hero">
  <div class="abs" role="img" aria-label="Photo of a trainer speaking to seated business people in a bright workshop room" style="inset:0"></div>
  <form class="upload-panel">
    <div class="upload-title">Upload your profile</div>
    <div class="upload-input">
      <svg width="14" height="14" viewBox="0 0 14 14"><circle cx="6" cy="6" r="4.5" fill="none" stroke="#9aa0a6" stroke-width="1.5"/><line x1="9.5" y1="9.5" x2="13" y2="13" stroke="#9aa0a6" stroke-width="1.5"/></svg>
      Browse...
    </div>
    <div class="upload-submit">Submit here!</div>
  </form>
  <div class="hero-dots"><span class="on"></span><span></span></div>
</section>

<section class="coaching">
  <p><strong>Coaching</strong>Lorem Ipsum is simply dummy text of the printing and typesetting industry. Lorem Ipsum has been the industry's standard dummy text ever since the 1500s, when an unknown printer took a galley</p>
  <a class="btn-outline">Get access</a>
</section>

<h2 class="section-title" style="top:744px">Gain access to training</h2>

<div class="feature" style="left:100px;top:822px">
  <svg viewBox="0 0 34 34"><ellipse cx="14" cy="13" rx="11" ry="8" fill="none" stroke="var(--blue)" stroke-width="2.5"/><path d="M8 20 L5 26 L13 21" fill="var(--blue)"/><path d="M22 19 a9 7 0 0 0 9 -5" fill="none" stroke="var(--blue)" stroke-width="2.5"/></svg>
  <h3>Simplemente el texto</h3>
  <p>Simplemente el texto de relleno de las imprentas y archivos de texto. Lorem Ipsum ha sido el texto de relleno estándar de las industrias...</p>
</div>
<div class="feature" style="left:444px;top:822px">
  <svg viewBox="0 0 34 34"><path d="M3 4 V30 H31" fill="none" stroke="var(--blue)" stroke-width="2.5"/><rect x="8" y="17" width="4" height="10" fill="var(--blue)"/><rect x="14" y="11" width="4" height="16" fill="var(--blue)"/><rect x="20" y="14" width="4" height="13" fill="var(--blue)"/><rect x="26" y="8" width="4" height="19" fill="var(--blue)"/></svg>
  <h3>Simplemente el texto</h3>
  <p>Simplemente el texto de relleno de las imprentas y archivos de texto. Lorem Ipsum ha sido el texto de relleno estándar de las industrias...</p>
</div>
<div class="feature" style="left:802px;top:822px">
  <svg viewBox="0 0 34 34"><circle cx="13" cy="20" r="8" fill="none" stroke="var(--blue)" stroke-width="5" stroke-dasharray="3 2.3"/><circle cx="13" cy="20" r="3" fill="var(--blue)"/><circle cx="26" cy="9" r="5" fill="none" stroke="var(--blue)" stroke-width="3.5" stroke-dasharray="2 1.8"/></svg>
  <h3>Simplemente el texto</h3>
  <p>Simplemente el texto de relleno de las imprentas y archivos de texto. Lorem Ipsum ha sido el texto de relleno estándar de las industrias...</p>
</div>
<div class="feature" style="left:100px;top:960px">
  <svg viewBox="0 0 34 34"><rect x="3" y="7" width="22" height="22" rx="3" fill="none" stroke="var(--blue)" stroke-width="2.5"/><path d="M14 20 L28 5 L31 8 L17 23 L13 24 Z" fill="var(--blue)"/></svg>
  <h3>Simplemente el texto</h3>
  <p>Simplemente el texto de relleno de las imprentas y archivos de texto. Lorem Ipsum ha sido el texto de relleno estándar de las industrias...</p>
</div>
<div class="feature" style="left:444px;top:960px">
  <svg viewBox="0 0 34 34"><rect x="2" y="5" width="30" height="19" rx="2" fill="none" stroke="var(--blue)" stroke-width="2.5"/><rect x="14" y="24" width="6" height="4" fill="var(--blue)"/><rect x="9" y="28" width="16" height="2.5" fill="var(--blue)"/></svg>
  <h3>Simplemente el texto</h3>
  <p>Simplemente el texto de relleno de las imprentas y archivos de texto. Lorem Ipsum ha sido el texto de relleno estándar de las industrias...</p>
</div>
<div class="feature" style="left:802px;top:960px">
  <svg viewBox="0 0 34 34"><path d="M7 3 H20 L27 10 V31 H7 Z" fill="none" stroke="var(--blue)" stroke-width="2.5"/><path d="M11 15 H23 M11 20 H23 M11 25 H23" stroke="var(--blue)" stroke-width="2"/></svg>
  <h3>Simplemente el texto</h3>
  <p>Simplemente el texto de relleno de las imprentas y archivos de texto. Lorem Ipsum ha sido el texto de relleno estándar de las industrias...</p>
</div>

<h2 class="section-title" style="top:1126px">Courses</h2>
<p class="section-sub" style="top:1168px">Lorem Ipsum is simply dummy text of the printing and typesetting industry has been the industry's standard dummy text ever</p>

<div class="thumb" style="left:100px;top:1234px;background:linear-gradient(135deg,#cfd8e2,#8fa2b8)" role="img" aria-label="Photo of a businessman presenting at a meeting table"></div>
<div class="thumb" style="left:356px;top:1234px;background:linear-gradient(135deg,#a9b59a,#6e7f6a)" role="img" aria-label="Photo of a team working together around a table"></div>
<div class="thumb" style="left:614px;top:1234px;background:linear-gradient(135deg,#6c6f73,#c9c2b8)" role="img" aria-label="Photo of hands typing on a laptop keyboard"></div>
<div class="thumb" style="left:870px;top:1234px;background:linear-gradient(135deg,#b7c6d6,#3e4a5a)" role="img" aria-label="Photo of business people meeting in an office lounge"></div>
<p class="thumb-caption" style="left:100px;top:1408px">Lorem Ipsum is simply dummy text of the printing and typesetting...</p>
<p class="thumb-caption" style="left:356px;top:1408px">Lorem Ipsum is simply dummy text of the printing and typesetting...</p>
<p class="thumb-caption" style="left:614px;top:1408px">Lorem Ipsum is simply dummy text of the printing and typesetting...</p>
<p class="thumb-caption" style="left:870px;top:1408px">Lorem Ipsum is simply dummy text of the printing and typesetting...</p>

<div class="thumb" style="left:100px;top:1494px;background:linear-gradient(135deg,#e3e6e8,#8a939c)" role="img" aria-label="Photo of a presenter at a whiteboard with a seated audience"></div>
<div class="thumb" style="left:356px;top:1494px;background:linear-gradient(135deg,#8b6a52,#3f3a38)" role="img" aria-label="Photo of colleagues reviewing papers at a desk"></div>
<div class="thumb" style="left:614px;top:1494px;background:linear-gradient(135deg,#d4d6d8,#55585c)" role="img" aria-label="Black and white photo of business people walking"></div>
<div class="thumb" style="left:870px;top:1494px;background:linear-gradient(135deg,#9fb0bf,#5a4a3a)" role="img" aria-label="Photo of cupped hands holding soil with a green seedling"></div>
<p class="thumb-caption" style="left:100px;top:1670px">Lorem Ipsum is simply dummy text of the printing and typesetting...</p>
<p class="thumb-caption" style="left:356px;top:1670px">Lorem Ipsum is simply dummy text of the printing and typesetting...</p>
<p class="thumb-caption" style="left:614px;top:1670px">Lorem Ipsum is simply dummy text of the printing and typesetting...</p>
<p class="thumb-caption" style="left:870px;top:1670px">Lorem Ipsum is simply dummy text of the printing and typesetting...</p>

<section class="news" role="img" aria-label="Blue-tinted background photo of people at a meeting">
  <h2 class="section-title">Latest news</h2>
  <p class="section-sub">Simplemente el texto de relleno de las imprentas y archivos de texto ha sido el texto de relleno estándar de las industrias desde el</p>
  <article class="news-card" style="left:100px"><h3>Lorem Ipsum is simply dummy text printing</h3><span class="news-date">27 November 2016</span><p>Simplemente el texto de relleno de las imprentas y archivos de texto. Lorem Ipsum ha sido el texto de relleno estándar de las industrias...</p></article>
  <article class="news-card" style="left:444px"><h3>Lorem Ipsum is simply dummy text printing</h3><span class="news-date">27 November 2016</span><p>Simplemente el texto de relleno de las imprentas y archivos de texto. Lorem Ipsum ha sido el texto de relleno estándar de las industrias...</p></article>
  <article class="news-card" style="left:788px"><h3>Lorem Ipsum is simply dummy text printing</h3><span class="news-date">27 November 2016</span><p>Simplemente el texto de relleno de las imprentas y archivos de texto. Lorem Ipsum ha sido el texto de relleno estándar de las industrias...</p></article>
</section>

<h2 class="section-title" style="top:2262px">Upcoming events</h2>
<p class="section-sub" style="top:2302px">Lorem Ipsum is simply dummy text of the printing and typesetting industry has been the industry's standard dummy text ever</p>

<div class="thumb" style="left:100px;top:2368px;background:linear-gradient(135deg,#cfe0ee,#3c4a5c)" role="img" aria-label="Photo of two business travellers walking by a private jet"></div>
<div class="thumb" style="left:356px;top:2368px;background:linear-gradient(135deg,#eef0f2,#9aa2aa)" role="img" aria-label="Photo of people at a long table in a bright office"></div>
<div class="thumb" style="left:614px;top:2368px;background:linear-gradient(135deg,#c6b9a6,#4a3e34)" role="img" aria-label="Photo of a woman working at a desk with a laptop"></div>
<div class="thumb" style="left:870px;top:2368px;background:linear-gradient(135deg,#e8e4df,#8a8580)" role="img" aria-label="Photo of a mentor and young professional looking at a laptop"></div>
<p class="thumb-caption" style="left:100px;top:2552px">Lorem Ipsum is simply dummy text</p>
<p class="thumb-caption" style="left:356px;top:2552px">Lorem Ipsum is simply dummy text</p>
<p class="thumb-caption" style="left:614px;top:2552px">Lorem Ipsum is simply dummy text</p>
<p class="thumb-caption" style="left:870px;top:2552px">Lorem Ipsum is simply dummy text</p>
<p class="event-date" style="left:100px;top:2576px">On 27 November 2016</p>
<p class="event-date" style="left:356px;top:2576px">On 27 November 2016</p>
<p class="event-date" style="left:614px;top:2576px">On 27 November 2016</p>
<p class="event-date" style="left:870px;top:2576px">On 27 November 2016</p>

<footer class="site-footer">
  <h4 class="foot-head" style="left:102px">Testimonials</h4>
  <span class="abs" style="left:364px;top:38px;font-size:13px;color:#9fb6cf">‹ &nbsp;›</span>
  <span class="quote-mark" style="left:100px;top:76px">“</span>
  <p class="quote">Simply dummy text of the printing and typesetting industry. Lorem Ipsum has been the industry's standard dummy text ever since the 1500s, when an unknown printer took a galley of type and scrambled it to make a type specimen book.</p>
  <span class="quote-mark" style="left:374px;top:176px">”</span>
  <p class="author"><b>Marcus Doyle</b>Marketing Executive</p>

  <h4 class="foot-head" style="left:504px">Welcome</h4>
  <ul class="foot-list" style="left:504px"><li>Home</li><li>About us</li><li>Services</li><li>News</li><li>Events</li><li>Courses</li><li>Contact us</li></ul>

  <h4 class="foot-head" style="left:704px">Information</h4>
  <ul class="foot-list" style="left:704px"><li>Privacy Policy</li><li>Terms &amp; Conditions</li><li>Sitemap</li></ul>

  <h4 class="foot-head" style="left:930px">Follow us</h4>
  <div class="social" style="top:66px"><span class="dot"></span>: Circlebook</div>
  <div class="social" style="top:106px"><span class="dot"></span>: Chirper</div>
  <div class="social" style="top:146px"><span class="dot"></span>: ProLink</div>
  <div class="social" style="top:186px"><span class="dot"></span>: Gather Plus</div>
</footer>
<div class="site-bottom">© 2016, The Harbor Loft. All rights reserved.</div>

</body>
</html>
```